Business Cards

I am a landscape designer and I am hired to do over the top landscapes!
I pay attention to detail and do everything from growing my own orchids and Fruits and Vegetables.
I build ponds water features. I do Landscape Lighting and Specialize in Drip Irrigation for New Landscapes.
I am looking for something with a picture of one of my landscapes and pictures of Orchids on the back so I can work on growing my Orchid business.
I like the plastic cards.
I like Saturation
I like color and I want something that really sticks out!
I will attach a few pics!
Thanks
Corey
A Bright Terrace LLC
Corey Nordvik
Orchids & Organic Farming
Landscaping Made Simple
555-203-4719
Abrightterrace@mailnest.example
Harbor Point FL

Target Market(s)

I work for Wealthy Clients who want unique designs and enjoy rare plants.
I am the goto guy for tropical and rare plants
Cool Designs
Orchids
Interior Decorating
Exterior Lighting
Organic Farming
People who appreciate plants

Industry/Entity Type

Landscape

Font styles to use
Decorative

Requirements
Must have
• COLOR COLOR COLOR
Saturation
Sleek and Clean
Should not have
• tacky

```html
<!DOCTYPE html>
<html lang="en">
<head>
<meta charset="utf-8">
<title>A Bright Terrace LLC – Business Cards</title>
<link href="https://fonts.googleapis.com/css2?family=Cormorant+Garamond:ital,wght@0,600;1,700&family=Questrial&display=swap" rel="stylesheet">
<style>
  :root {
    --page: #e9e6ee;
    --card-black: #111113;
    --card-black-2: #1d1d22;
    --lavender: #e6e0f1;
    --lavender-deep: #d3c8e8;
    --purple: #6b3fa0;
    --purple-band: #7e4bb8;
    --purple-text: #8a5cc4;
    --white: #ffffff;
  }
  * { margin: 0; padding: 0; box-sizing: border-box; }
  html, body { width: 1200px; height: 784px; overflow: hidden; }
  body {
    background: var(--page);
    display: flex;
    align-items: center;
    justify-content: center;
    gap: 30px;
  }
  .card {
    position: relative;
    width: 560px;
    height: 320px;
    overflow: hidden;
    box-shadow: 0 6px 18px rgba(0,0,0,.22);
  }
  /* ---------- back of card ---------- */
  .card-back { background: radial-gradient(circle at 60% 60%, var(--card-black-2), var(--card-black)); }
  .card-back svg { position: absolute; inset: 0; }
  .back-wordmark {
    position: absolute;
    left: 300px;
    top: 238px;
    font-family: "Cormorant Garamond", serif;
    font-weight: 600;
    font-size: 26px;
    line-height: 1;
    color: var(--purple-text);
    white-space: nowrap;
  }
  /* ---------- front of card ---------- */
  .card-front { background: var(--card-black); }
  .front-top {
    position: absolute;
    left: 0; right: 0; top: 0;
    height: 150px;
    background: linear-gradient(135deg, var(--lavender), var(--lavender-deep) 60%, var(--lavender));
  }
  .front-wordmark {
    position: absolute;
    left: 0; right: 0;
    top: 48px;
    text-align: center;
    font-family: "Cormorant Garamond", serif;
    font-weight: 600;
    font-size: 46px;
    line-height: 1;
    color: var(--purple);
    white-space: nowrap;
  }
  .tagline-band {
    position: absolute;
    left: 0; right: 0;
    top: 150px;
    height: 22px;
    background: var(--purple-band);
    font-family: "Cormorant Garamond", serif;
    font-style: italic;
    font-weight: 700;
    font-size: 16px;
    line-height: 22px;
    color: var(--lavender);
    padding-left: 22px;
    white-space: nowrap;
  }
  .front-bottom {
    position: absolute;
    left: 0; right: 0; bottom: 0;
    height: 148px;
    background: radial-gradient(circle at 70% 40%, var(--card-black-2), var(--card-black));
  }
  .holder-name {
    position: absolute;
    left: 26px;
    top: 180px;
    font-family: "Cormorant Garamond", serif;
    font-weight: 600;
    font-size: 27px;
    line-height: 1.2;
    color: var(--purple-text);
  }
  .contact-list {
    position: absolute;
    left: 26px;
    top: 226px;
    list-style: none;
    font-family: "Questrial", sans-serif;
    font-size: 17px;
    color: var(--white);
  }
  .contact-list li { display: flex; align-items: center; gap: 8px; height: 26px; white-space: nowrap; }
  .contact-list svg { width: 16px; height: 16px; fill: var(--purple-text); flex: none; }
</style>
</head>
<body>

<section class="card card-back" aria-label="Card back">
  <svg viewBox="0 0 560 320" width="560" height="320">
    <defs>
      <linearGradient id="gardenTones" x1="0" y1="0" x2="1" y2="1">
        <stop offset="0" stop-color="#9fb86a"/>
        <stop offset=".35" stop-color="#c45a3a"/>
        <stop offset=".6" stop-color="#4c7d34"/>
        <stop offset="1" stop-color="#1f4a18"/>
      </linearGradient>
      <radialGradient id="orchidTones" cx=".45" cy=".45" r=".6">
        <stop offset="0" stop-color="#a87ae6"/>
        <stop offset=".6" stop-color="#7a48c8"/>
        <stop offset="1" stop-color="#3f3a35"/>
      </radialGradient>
    </defs>
    <path d="M0 0 H200 C300 50 310 250 200 320 H0 Z" fill="url(#gardenTones)" stroke="#7e4bb8" stroke-width="3" role="img" aria-label="Photograph of a lush flower garden with purple, red and white blooms"/>
    <circle cx="440" cy="80" r="128" fill="url(#orchidTones)" stroke="#7e4bb8" stroke-width="3" role="img" aria-label="Photograph of purple spotted orchid blossoms"/>
  </svg>
  <div class="back-wordmark">A Bright Terrace LLC</div>
</section>

<section class="card card-front" aria-label="Card front">
  <div class="front-top" role="img" aria-label="Soft lavender damask background"></div>
  <div class="front-wordmark">A Bright Terrace LLC</div>
  <div class="tagline-band">Rare Orchids &amp; Home Harvests | Gardens Made Easy</div>
  <div class="front-bottom"></div>
  <div class="holder-name">Corey Nordvik</div>
  <ul class="contact-list">
    <li>
      <svg viewBox="0 0 24 24" aria-hidden="true"><path d="M6.6 10.8a15 15 0 0 0 6.6 6.6l2.2-2.2a1 1 0 0 1 1-.25 11.4 11.4 0 0 0 3.6.57 1 1 0 0 1 1 1V20a1 1 0 0 1-1 1A17 17 0 0 1 3 4a1 1 0 0 1 1-1h3.5a1 1 0 0 1 1 1c0 1.25.2 2.45.57 3.57a1 1 0 0 1-.25 1z"/></svg>
      555-203-4719
    </li>
    <li>
      <svg viewBox="0 0 24 24" aria-hidden="true"><path d="M3 5h18a1 1 0 0 1 1 1v12a1 1 0 0 1-1 1H3a1 1 0 0 1-1-1V6a1 1 0 0 1 1-1zm1 2.2V17h16V7.2l-8 5.3z M4.6 7l7.4 4.9L19.4 7z"/></svg>
      Abrightterrace@mailnest.example
    </li>
    <li>
      <svg viewBox="0 0 24 24" aria-hidden="true"><path d="M12 3l10 9h-3v9h-5v-6h-4v6H5v-9H2z"/></svg>
      Harbor Point FL
    </li>
  </ul>
</section>

</body>
</html>
```